Live at Belvane Playhouse Concert Series

Belvane Playhouse Concert Series

Febraury 1st - Peter Daws Hallam (Garland Winner, Harbor Kings)
March 1st - Celia Varnum (Silver Crest Winner, The Willow)
April 5th - Rosalind Pike (A Toast to Mabel: The First Seasons)
May 3rd - Justine Corvell (Garland Nominee, Poppy)

All shows at 7:30PM

Subscribe to the series and save 10%

Get your tickets online at www.belvanestages.example

Poster size 11" X 17" also 27" x 41"

Target Market(s)

Upscale market and music lovers. Small venue with international performers

Colors

Designer to choose colors to be used in the design.

Requirements
Must have
• Upscale - rich - style - like LUXE
Should not have
• Clip art

```html
<!DOCTYPE html>
<html lang="en">
<head>
<meta charset="utf-8">
<title>Belvane Playhouse Concert Series</title>
<link rel="stylesheet" href="https://fonts.googleapis.com/css2?family=Inter:wght@400;600;700;800&display=swap">
<style>
  :root {
    --backdrop: #6e6e6e;
    --ink: #000;
    --paper: #fff;
    --cyan: #12a9e0;
    --green: #3aae49;
    --orange: #f5a71c;
    --magenta: #e0168a;
    --gold: #f5b21c;
  }
  * { box-sizing: border-box; margin: 0; padding: 0; }
  html, body { width: 1200px; height: 1200px; overflow: hidden; }
  body {
    background: var(--backdrop);
    font-family: "Inter", Arial, sans-serif;
    display: flex; align-items: center; justify-content: center;
  }
  .poster {
    width: 800px; height: 1124px;
    background: var(--ink);
    display: flex; flex-direction: column;
    position: relative;
  }
  .hero {
    height: 592px; position: relative; overflow: hidden;
  }
  .hero-photo {
    position: absolute; inset: 0;
    background:
      radial-gradient(ellipse 60% 30% at 70% 82%, rgba(235,245,240,.85), rgba(120,200,190,.35) 55%, transparent 75%),
      radial-gradient(ellipse 30% 40% at 55% 55%, rgba(200,40,90,.55), transparent 70%),
      radial-gradient(ellipse 35% 30% at 95% 20%, rgba(30,70,40,.6), transparent 70%),
      linear-gradient(180deg, #050510 0%, #120c3a 45%, #2a1450 70%, #3a2a3a 100%);
  }
  .title {
    position: absolute; left: 46px; top: 38px;
    font-weight: 800; font-size: 104px; line-height: 92px;
    letter-spacing: -5px;
  }
  .title-line { display: block; color: var(--paper); }
  .title-line.accent {
    color: var(--magenta);
    -webkit-text-stroke: 3px var(--paper);
    paint-order: stroke fill;
  }
  .lineup {
    display: flex; gap: 10px; padding: 0 2px;
    height: 360px;
  }
  .act { flex: 1; display: flex; flex-direction: column; }
  .act-head {
    height: 94px; color: var(--paper); text-align: center;
    padding-top: 10px; line-height: 1.15;
  }
  .act-date { font-size: 16px; font-weight: 400; }
  .act-name { font-size: 16px; font-weight: 700; letter-spacing: .2px; white-space: nowrap; }
  .act-note { font-size: 11px; margin-top: 3px; }
  .act-show { font-size: 13px; }
  .act--cyan .act-head { background: var(--cyan); }
  .act--green .act-head { background: var(--green); }
  .act--orange .act-head { background: var(--orange); }
  .act--magenta .act-head { background: var(--magenta); }
  .act-photo { flex: 1; }
  .act--cyan .act-photo { background: linear-gradient(160deg, #f4f4f6, #dfe3ea); }
  .act--green .act-photo { background: linear-gradient(160deg, #6a6a6a, #2a2a2a 70%, #111); }
  .act--orange .act-photo { background: linear-gradient(160deg, #4a2a20, #7a2a22 50%, #1c1410); }
  .act--magenta .act-photo { background: linear-gradient(160deg, #f3e4ee, #e6c9db 60%, #c9a0b8); }
  .showtime {
    height: 46px; display: flex; align-items: center; justify-content: center;
    color: var(--gold); font-weight: 700; font-size: 21px; letter-spacing: 4px;
  }
  .footer {
    flex: 1; position: relative; color: var(--paper); text-align: center;
    background:
      linear-gradient(90deg, rgba(190,140,80,.55), rgba(60,120,150,.45) 25%, rgba(200,180,120,.4) 50%, rgba(190,60,90,.5) 75%, rgba(130,150,60,.5)),
      linear-gradient(180deg, #3a3a3a, #1e1e1e);
  }
  .footer-text {
    position: absolute; inset: 0;
    display: flex; flex-direction: column; justify-content: center; gap: 18px;
    font-weight: 600; font-size: 19px; letter-spacing: .3px;
  }
</style>
</head>
<body>
  <main class="poster">
    <section class="hero">
      <div class="hero-photo" role="img" aria-label="Night photograph of the playhouse facade with its glowing neon marquee"></div>
      <h1 class="title">
        <span class="title-line">Belvane</span>
        <span class="title-line">Playhouse</span>
        <span class="title-line accent">Concert</span>
        <span class="title-line accent">Series</span>
      </h1>
    </section>

    <section class="lineup">
      <article class="act act--cyan">
        <header class="act-head">
          <div class="act-date">Febraury 1st</div>
          <div class="act-name">PETER DAWS HALLAM</div>
          <div class="act-note">Garland Winner</div>
          <div class="act-show">Harbor Kings</div>
        </header>
        <div class="act-photo" role="img" aria-label="Portrait of Peter Daws Hallam in a white shirt"></div>
      </article>
      <article class="act act--green">
        <header class="act-head">
          <div class="act-date">March 1st</div>
          <div class="act-name">CELIA VARNUM</div>
          <div class="act-note">Silver Crest Winner</div>
          <div class="act-show">The Willow</div>
        </header>
        <div class="act-photo" role="img" aria-label="Portrait of Celia Varnum in a dark beaded top"></div>
      </article>
      <article class="act act--orange">
        <header class="act-head">
          <div class="act-date">April 5th</div>
          <div class="act-name">ROSALIND PIKE</div>
          <div class="act-note">A Toast to Mabel</div>
          <div class="act-show">The First Seasons</div>
        </header>
        <div class="act-photo" role="img" aria-label="Portrait of Rosalind Pike before a red curtain"></div>
      </article>
      <article class="act act--magenta">
        <header class="act-head">
          <div class="act-date">May 3rd</div>
          <div class="act-name">JUSTINE CORVELL</div>
          <div class="act-note">Garland Nominee</div>
          <div class="act-show">Poppy</div>
        </header>
        <div class="act-photo" role="img" aria-label="Portrait of Justine Corvell on a soft pink background"></div>
      </article>
    </section>

    <div class="showtime">ALL SHOWS AT 7:30PM</div>

    <footer class="footer" role="img" aria-label="Colourful reflections on the polished lobby floor">
      <div class="footer-text">
        <p>Subscribe to the series and save 10%</p>
        <p>Get your tickets online at www.belvanestages.example</p>
      </div>
    </footer>
  </main>
</body>
</html>
```